Trying to make a small (4.25" x 5.50") re-elect sticker for a congressman in california. The congressmans name is Calder Voss and we would like to change his last name to "Vossovich". Basically we believe his relationship to Pike/Brevik should be reflected in this poster with russia undertones.

The idea behind this project is to reflect Calder Voss as a political puppet of Harlan Pike who is also a puppet of Russian president Brevik.
We do not support Calder Voss as our elected official and believe him to be a traitor to our district and a traitor to our country.
Trying to make a small (4.25" x 5.50") re-elect sticker for a congressman in California. The congressman's name is Calder Voss and we would like to change his last name to "Vossovich". Basically we believe his relationship to Pike/Brevik should be reflected in this poster with Russia undertones.

Trying to make a small (4.25" x 5.50") re-elect sticker for a congressman in California. The congressman's name is Calder Voss and we would like to change his last name to "Vossovich". Basically we believe his relationship to Pike/Brevik should be reflected in this poster with Russian undertones.

I have never done this type of project before so any advise would be helpful,any questions just email me thanks.
Owen

Owen

Target Market(s)

For political grass roots campaign.

Industry/Entity Type

Political

Colors

Designer to choose colors to be used in the design.

Requirements
Must have
• Picture of Calder Voss. Re-elect (переизбрание). Change last name to Vossovich
Nice to have
• Maybe the hammer and sickle logo someplace but not too obvious
Should not have
• Nothing obscene or offensiveпереизбрание

```html
<!DOCTYPE html>
<html lang="en">
<head>
<meta charset="utf-8">
<title>Calder Vossovich — Re-elect Sticker</title>
<link href="https://fonts.googleapis.com/css2?family=Anton&family=Archivo+Black&family=Open+Sans:wght@400&display=swap" rel="stylesheet">
<style>
  :root {
    --red-bright: #ff0a05;
    --red-main: #e01410;
    --red-deep: #b82a22;
    --rust: #8a3a22;
    --banner-red: #870000;
    --ink: #1a0606;
    --white: #ffffff;
    --pink-fade: #f2a0a0;
  }
  html, body {
    margin: 0;
    padding: 0;
    width: 1200px;
    height: 923px;
    overflow: hidden;
    background: var(--white);
  }
  .sticker {
    position: relative;
    width: 1200px;
    height: 923px;
    overflow: hidden;
  }
  .sticker__art {
    position: absolute;
    inset: 0;
    display: block;
  }
  .headline {
    font-family: "Anton", "Oswald", sans-serif;
  }
  .subline {
    font-family: "Open Sans", "Noto Sans", sans-serif;
  }
  .cta {
    font-family: "Archivo Black", "Arial Black", sans-serif;
  }
</style>
</head>
<body>
<main class="sticker">
  <svg class="sticker__art" viewBox="0 0 1200 923" width="1200" height="923" xmlns="http://www.w3.org/2000/svg">
    <defs>
      <linearGradient id="bg-base" x1="0" y1="1" x2="1" y2="0">
        <stop offset="0" stop-color="var(--red-bright)"/>
        <stop offset="0.55" stop-color="var(--red-main)"/>
        <stop offset="1" stop-color="var(--red-deep)"/>
      </linearGradient>
      <linearGradient id="backdrop-tone" x1="0" y1="0" x2="1" y2="1">
        <stop offset="0" stop-color="#a83a2a" stop-opacity="0.85"/>
        <stop offset="0.5" stop-color="#b8281c" stop-opacity="0.7"/>
        <stop offset="1" stop-color="var(--rust)" stop-opacity="0.9"/>
      </linearGradient>
      <linearGradient id="portrait-tone" x1="0" y1="0" x2="0" y2="1">
        <stop offset="0" stop-color="#3a0c08" stop-opacity="0.85"/>
        <stop offset="1" stop-color="var(--ink)" stop-opacity="0.95"/>
      </linearGradient>
      <linearGradient id="title-fade" x1="0" y1="0" x2="1" y2="0.6">
        <stop offset="0" stop-color="var(--white)"/>
        <stop offset="0.5" stop-color="var(--white)"/>
        <stop offset="0.62" stop-color="var(--pink-fade)"/>
        <stop offset="1" stop-color="#fbe3e3"/>
      </linearGradient>
    </defs>

    <!-- base -->
    <rect class="bg-base" width="1200" height="923" fill="url(#bg-base)"/>

    <!-- backdrop scene area -->
    <rect class="backdrop" x="300" y="0" width="900" height="760" fill="url(#backdrop-tone)"
          role="img" aria-label="Backdrop photo of a red star emblem in warm red and rust tones"/>

    <!-- diagonal light bands -->
    <polygon class="band" points="0,0 90,0 0,90" fill="#ffffff" opacity="0.08"/>
    <polygon class="band" points="0,330 560,0 760,0 0,560" fill="#ffffff" opacity="0.06"/>
    <polygon class="band" points="0,700 820,140 1000,140 0,860" fill="#ff3a30" opacity="0.18"/>

    <!-- portrait area -->
    <path class="portrait" d="M60 923 L60 330 Q60 60 300 60 Q546 60 546 330 L546 923 Z" fill="url(#portrait-tone)"
          role="img" aria-label="Stencil portrait of the candidate in black on red"/>

    <!-- white corner -->
    <polygon class="corner" points="1200,490 1200,923 675,923" fill="var(--white)"/>

    <!-- headline -->
    <text class="headline" x="600" y="228" font-size="168" fill="url(#title-fade)"
          textLength="400" lengthAdjust="spacingAndGlyphs">Calder</text>
    <text class="headline" x="600" y="395" font-size="168" fill="url(#title-fade)"
          textLength="578" lengthAdjust="spacingAndGlyphs">Vossovich</text>
    <text class="subline" x="604" y="478" font-size="68" fill="var(--white)"
          textLength="542" lengthAdjust="spacingAndGlyphs">переизбрание</text>

    <!-- re-elect banner -->
    <rect class="banner" x="603" y="630" width="545" height="185" fill="var(--banner-red)"/>
    <polygon class="banner-tail" points="1005,815 1148,815 1008,859" fill="var(--banner-red)"/>
    <text class="cta" x="624" y="764" font-size="112" fill="var(--white)"
          textLength="494" lengthAdjust="spacingAndGlyphs">Re-elect</text>
  </svg>
</main>
</body>
</html>
```